Website for Reiki and Wellness Courses

I teach online courses in Reiki and wellness/self-development and am needing a new website.

The focus of the website will be to provide descriptions of the courses as well as include a blog and pages where students in my courses will visit for additional information.

Note: courses are NOT hosted on this site.
The focus of this website will be to encourage viewers to enroll in courses as well as opt in to the email list.

I will upload copy soon. My old website is: http://brightmeadowstudies.example. Please do not use existing logo.

Target Market(s)

Alternative health, wellness, spirituality, personal development. Males and females of all ages seeking to improve their health and life.

Industry/Entity Type

Health And Wellness

Logo Text

No text (please do not use existing logo)

Coding

Coded - Design and coding required

Number of Pages Required

5+ page

Requirements
Must have
• 1. Home page
• 2. About page
• 3. Courses page that outlines courses (there are currently 6 courses with 1 coming soon)
• 4. Individual course page (maybe a template that I can adjust color and pictures for with each course)
• 5. Blog
• 6. Student Area that outlines all Student Areas
• 7. Individual Student Area page (maybe a template that I can adjust color and pictures for with each course)
• 8. Shop page (note: items will not currently be purchased through website - it will be a link to quillmart for a book).
• 9. Student thank-you page (maybe a template that I can adjust color and pictures for with each course) this is the page students are directed to at end of course with vouchers for other courses.
• Opt-in for the home page, course pages, blog and thank-you pages
Nice to have
• I would like the design to be calm, clean and soothing. Ideally visitors feel relaxed when viewing the site and are encouraged to explore the courses, subscribe to the email list and purchase a product.
• ~ Testimonials page
• ~ Contact page
• I tend to gravitate towards blues, greys and purples as well as monochromatic color schemes.
Should not have
• Contact form on home page
• phone number on home page
• location/physical address
• dates for blog posts

```html
<!DOCTYPE html>
<html lang="en">
<head>
<meta charset="utf-8">
<title>Bright Meadow Studies</title>
<link href="https://fonts.googleapis.com/css2?family=Montserrat:wght@300;400;500;600;700&display=swap" rel="stylesheet">
<style>
:root{
  --slate:#6b7397;
  --slate-dark:#585f80;
  --navy:#2b3250;
  --green:#47a51c;
  --ink:#222;
  --muted:#8a8a8a;
  --line:#e8e8e8;
  --footer:#f4f4f4;
  --diamond-edge:#4a55b3;
}
*{box-sizing:border-box;margin:0;padding:0}
html,body{width:1200px;height:2442px;overflow:hidden;background:#fff}
body{font-family:'Montserrat',sans-serif;color:var(--ink);position:relative}
.abs{position:absolute}
.center{text-align:center}

/* header */
.site-header{position:absolute;left:0;top:0;width:1200px;height:114px;background:#fff}
.brand{position:absolute;display:flex;align-items:center;gap:12px;font-size:20px;font-weight:500;color:var(--slate)}
.brand-mark{width:22px;height:22px;background:var(--slate)}
.main-nav a{position:absolute;top:53px;font-size:11px;font-weight:600;color:#222;text-decoration:none;letter-spacing:.3px;transform:translateX(-50%)}
.nav-active{position:absolute;left:562px;top:59px;width:46px;height:46px;background:var(--slate);transform:translate(-50%,-50%) rotate(45deg)}
.main-nav a.current{color:#fff}
.search-icon{position:absolute;left:970px;top:51px}

/* hero */
.hero{position:absolute;left:0;top:114px;width:1200px;height:500px;overflow:hidden}
.hero-photo{position:absolute;inset:0;background:linear-gradient(180deg,#f3f0dc 0%,#cfe1d6 35%,#6fa3a2 60%,#3f7f85 100%)}
.hero-triangle{position:absolute;left:0;top:0}
.hero-copy{position:absolute;left:585px;width:400px;top:120px;color:#fff;text-align:center}
.hero-title{font-size:44px;font-weight:400;line-height:46px}
.hero-title b{font-weight:700}
.hero-sub{font-size:19px;font-weight:400;line-height:28px;margin-top:20px}
.btn{display:inline-block;background:var(--green);color:#fff;font-family:inherit;text-decoration:none;text-align:center}
.hero-btn{position:absolute;left:700px;top:327px;width:171px;height:52px;line-height:52px;font-size:18px;font-weight:500;letter-spacing:.5px}
.slider-dots span{position:absolute;left:31px;width:12px;height:12px;border-radius:50%;background:#fff}
.slider-dots span.on{background:var(--diamond-edge)}

/* provide */
.section-title{position:absolute;left:0;width:1200px;text-align:center}
.provide-title{top:686px;font-size:23px;font-weight:500;color:var(--slate);letter-spacing:.5px}
.offer{position:absolute;width:260px;text-align:center;transform:translateX(-50%)}
.offer-thumb{position:absolute;width:166px;height:166px;border:4px solid var(--diamond-edge);transform:translate(-50%,-50%) rotate(45deg)}
.offer h3{font-size:14px;font-weight:600;line-height:23px;color:#111;letter-spacing:.2px}
.offer p{font-size:11px;line-height:23px;color:var(--muted);margin:0 auto;width:250px}

/* subscribe */
.subscribe{position:absolute;left:0;top:1237px;width:1200px;height:422px;background:linear-gradient(90deg,#262d49 0%,#2e3554 55%,#3b4260 100%)}
.subscribe h2{position:absolute;left:0;width:1200px;top:68px;text-align:center;color:#fff;font-size:39px;font-weight:400}
.subscribe p{position:absolute;left:210px;width:780px;top:144px;text-align:center;color:#fff;font-size:14px;line-height:27px}
.field{position:absolute;top:241px;width:250px;height:47px;border:1px solid #c9ccd8;border-radius:3px;color:#b6b9c8;font-size:9px;padding-left:13px;line-height:45px;letter-spacing:.3px}
.subscribe-btn{position:absolute;left:521px;top:324px;width:158px;height:46px;line-height:46px;font-size:14px;font-weight:700;border-radius:2px}

/* testimonials */
.testimonials-title{top:1730px;font-size:40px;font-weight:400;color:var(--slate)}
.quote-badge{position:absolute;left:556px;top:1822px;width:90px;height:90px;border-radius:50%;background:var(--slate);color:#fff;font-size:70px;font-weight:700;text-align:center;line-height:112px}
.quote-line{top:1932px;font-size:24px;font-weight:400;color:#111}
.quote-name{top:1976px;font-size:18px;color:var(--green)}
.quote-rule{position:absolute;left:485px;top:2021px;width:212px;height:2px;background:var(--slate)}
.quote-body{position:absolute;left:200px;width:800px;top:2045px;text-align:center;font-size:11px;line-height:22.6px;color:#444}
.slide-arrow{position:absolute;top:1937px}

/* footer */
.site-footer{position:absolute;left:0;top:2242px;width:1200px;height:200px;background:var(--footer);border-top:1px solid var(--line)}
.footer-nav a{position:absolute;top:109px;font-size:11px;font-weight:600;color:#222;text-decoration:none;transform:translateX(-50%)}
.copyright{position:absolute;left:0;width:1200px;top:146px;text-align:center;font-size:10px;font-weight:600;color:#222;letter-spacing:.3px}
</style>
</head>
<body>

<header class="site-header">
  <div class="brand" style="left:196px;top:47px"><span class="brand-mark"></span>Bright Meadow Studies</div>
  <span class="nav-active"></span>
  <nav class="main-nav">
    <a class="current" href="#" style="left:562px">ABOUT</a>
    <a href="#" style="left:645px">COURSES</a>
    <a href="#" style="left:739px">STUDENT AREAS</a>
    <a href="#" style="left:842px">BLOG</a>
    <a href="#" style="left:912px">CONTACT</a>
  </nav>
  <svg class="search-icon" width="14" height="14" viewBox="0 0 14 14"><circle cx="5.5" cy="5.5" r="4" fill="none" stroke="#4a55b3" stroke-width="2"/><line x1="8.5" y1="8.5" x2="12.5" y2="12.5" stroke="#4a55b3" stroke-width="2"/></svg>
</header>

<section class="hero">
  <div class="hero-photo" role="img" aria-label="Woman in a sun hat with arms open wide beside a calm sea"></div>
  <svg class="hero-triangle" width="1200" height="500" viewBox="0 0 1200 500"><polygon points="466,0 1107,0 716,500" fill="#4a5274" fill-opacity="0.92"/></svg>
  <div class="hero-copy">
    <h1 class="hero-title">Time for Change<br>in Your <b>Life</b></h1>
    <p class="hero-sub">What would it be like to live the<br>life you were meant to live?</p>
  </div>
  <a class="btn hero-btn" href="#">LEARN MORE</a>
  <div class="slider-dots">
    <span style="top:368px"></span><span style="top:393px"></span><span style="top:416px"></span><span class="on" style="top:440px"></span>
  </div>
</section>

<h2 class="section-title provide-title">WHAT WE PROVIDE</h2>

<div class="offer-thumb" style="left:326px;top:873px;background:linear-gradient(135deg,#a9b6e6,#7fa35a)" role="img" aria-label="Person leaping joyfully on a green meadow"></div>
<div class="offer-thumb" style="left:601px;top:873px;background:linear-gradient(135deg,#9cc65a,#3f7426)" role="img" aria-label="Young green plant beside a quality of life note"></div>
<div class="offer-thumb" style="left:874px;top:873px;background:linear-gradient(135deg,#d99a5a,#6a7fb6)" role="img" aria-label="Man with arms raised towards a bright sky"></div>

<div class="offer" style="left:326px;top:1003px">
  <h3>HOW REIKI WORKS</h3>
  <p style="margin-top:46px">Reiki has been used for centuries to help individuals with physical and emotional imbalances as well as those seeking clarity and enlightenment.</p>
</div>
<div class="offer" style="left:601px;top:1003px">
  <h3>TRADITIONAL USUI REIKI MASTER CERTIFICATION</h3>
  <p style="margin-top:23px">Reiki has been used for centuries to help individuals with physical and emotional imbalances as well as those seeking clarity and enlightenment.</p>
</div>
<div class="offer" style="left:874px;top:1003px">
  <h3>RESOURCES</h3>
  <p style="margin-top:46px">Reiki has been used for centuries to help individuals with physical and emotional imbalances as well as those seeking clarity and enlightenment.</p>
</div>

<section class="subscribe">
  <h2>Stay Inspired</h2>
  <p>Receive information and articles each month to keep you feeling inspired. As a thank-you, you will also receive access to soothing music you can download for use in your Reiki sessions and meditation.</p>
  <div class="field" style="left:200px">FIRST NAME</div>
  <div class="field" style="left:477px">LAST NAME</div>
  <div class="field" style="left:752px">E-MAIL ADDRESS</div>
  <a class="btn subscribe-btn" href="#">YES-COUNT IN</a>
</section>

<h2 class="section-title testimonials-title">Testimonials</h2>
<div class="quote-badge">&ldquo;</div>
<p class="section-title quote-line">So glad I decided to take this course! Well presented and great value.</p>
<p class="section-title quote-name">Marla Quinn</p>
<div class="quote-rule"></div>
<p class="quote-body">I've long been interested in Reiki, but found the costs of local workshops prohibitive. I was initially skeptical of an online Reiki class, as I am aware of the controversy surrounding distant attunement. I decided, though, that the educational component was worth the investment even if the attunement process was less effective. I'm so glad I took the class despite that initial hesitation! Not only was the information very well-presented and easy to follow, but Nora was helpful and accessible to those who had questions. And the attunements I received left no question as to effectiveness. While everyone's subjective experience of Reiki and the attunement process will be individual, I have developed a sensitivity to energy flows from my Tarot practice and found the attunements intense and moving. I would not hesitate to recommend this course to anyone who wants to learn Reiki. Thank you, Nora!</p>

<svg class="slide-arrow" style="left:0" width="62" height="112" viewBox="0 0 62 112"><polygon points="0,0 62,56 0,112" fill="#ececec"/><polyline points="28,46 18,56 28,66" fill="none" stroke="#333" stroke-width="2"/></svg>
<svg class="slide-arrow" style="left:1138px" width="62" height="112" viewBox="0 0 62 112"><polygon points="62,0 0,56 62,112" fill="#ececec"/><polyline points="34,46 44,56 34,66" fill="none" stroke="#333" stroke-width="2"/></svg>

<footer class="site-footer">
  <div class="brand" style="left:487px;top:40px"><span class="brand-mark"></span>Bright Meadow Studies</div>
  <nav class="footer-nav">
    <a href="#" style="left:429px">ABOUT</a>
    <a href="#" style="left:506px">COURSES</a>
    <a href="#" style="left:601px">STUDENT AREAS</a>
    <a href="#" style="left:703px">BLOG</a>
    <a href="#" style="left:772px">CONTACT</a>
  </nav>
  <p class="copyright">© 2016 BRIGHT MEADOW STUDIES | ALL RIGHTS RESERVED</p>
</footer>

</body>
</html>
```